Resume: Professional Marketer seeking to impress potential recruiters with my skills & experience

Create a marketing esque style CV. I'm an outgoing, driven marketing with years of experience. I'm looking for a new senior role. My CV should look professional, but with elements of creativity and be a little bold. It should stand out amongst all the other CVs being submitted for a role. Check out my workfolio profile here: https://www.careerlinkspace.net/in/morwenna-traske-58291604/ I would like to include a photo with the design, as a subtle element of the design.

Target Market(s)

Recruiters, Headhunters

Industry/Entity Type

Marketing

Font styles to use
Sans Serif

Requirements
Must have
• Easy to read sections, with enough detail for a recruiter to understand my experience.
Nice to have
• Graphics, icons etc to represent experience

```html
<!DOCTYPE html>
<html lang="en">
<head>
<meta charset="utf-8">
<title>Morwenna Traske – Curriculum Vitae</title>
<link rel="stylesheet" href="https://fonts.googleapis.com/css2?family=Arimo:wght@400;700&family=Tinos:ital,wght@0,400;0,700;1,400;1,700&display=swap">
<style>
:root{
  --blue-deep:#17408f;
  --blue-mid:#2560bd;
  --blue-light:#3c7fd9;
  --page:#dde1e7;
  --cell:#ffffff;
  --head-cell:#c9ced6;
  --rule:#9aa1ab;
  --ink:#1b1b1b;
  --white:#ffffff;
}
*{box-sizing:border-box;margin:0;padding:0}
html,body{width:759px;height:1200px;overflow:hidden}
body{background:var(--page);font-family:"Tinos",serif;color:var(--ink);position:relative}
.cv-header{position:absolute;left:0;top:0;width:759px;height:405px;
  background:linear-gradient(160deg,var(--blue-deep) 0%,var(--blue-mid) 55%,var(--blue-light) 100%);}
.cv-header .wave{position:absolute;left:0;bottom:0;width:759px;height:40px}
.identity{position:absolute;left:34px;top:28px;color:var(--white)}
.identity .name{font-family:"Arimo",sans-serif;font-weight:700;font-size:31px;letter-spacing:.5px}
.identity .contact{font-family:"Arimo",sans-serif;font-weight:700;font-size:13px;margin-top:6px}
.portrait{position:absolute;left:448px;top:10px;width:112px;height:112px;border-radius:50%;
  border:3px solid var(--white);background:radial-gradient(circle at 50% 40%,#f0d6c2 0%,#c99f86 55%,#7d8fae 100%)}
.intro{position:absolute;left:34px;top:120px;width:690px;color:var(--white)}
.intro h2{font-family:"Tinos",serif;font-weight:700;font-style:italic;font-size:16px;letter-spacing:.5px;margin-bottom:12px}
.intro p{font-style:italic;font-size:13.6px;line-height:1.3;margin-bottom:12px}
.employment{position:absolute;left:30px;top:420px;width:699px;border-collapse:collapse;font-size:12px;line-height:1.25}
.employment td,.employment th{border:1px solid var(--rule);padding:3px 6px;vertical-align:top;text-align:left;background:var(--cell)}
.employment .title th{background:var(--head-cell);font-weight:700;font-size:12.5px;height:24px}
.employment .cols th{background:var(--head-cell);font-weight:700;height:22px}
.employment tbody td{height:44px}
.col-dates{width:104px}
.col-role{width:278px}
</style>
</head>
<body>
<header class="cv-header">
  <svg class="wave" viewBox="0 0 759 40" preserveAspectRatio="none" aria-hidden="true">
    <path d="M0 40 L0 22 C180 2 420 38 759 10 L759 40 Z" fill="var(--page)"/>
  </svg>
  <div class="identity">
    <div class="name">Morwenna Traske</div>
    <div class="contact">Avalon Bay NSW 0400 318 527</div>
  </div>
  <div class="portrait" role="img" aria-label="Portrait photo of Morwenna Traske"></div>
  <section class="intro">
    <h2>INTRODUCTION</h2>
    <p>I am a passionate direct marketer of 15+ years experience in Australia, plus key roles in startup organisations in London and New York.</p>
    <p>I am a talented consumer marketer with strong commercial and business acumen. I played a fundamental role in the growth of CoverDirect Pty Ltd, to become the number one direct life insurance brand in Australia.</p>
    <p>As a strategic marketer, my strengths lie in analytical thinking and the ability to translate marketing and sales activity into commercial modeling, and ultimately profitability.</p>
    <p>I am a talented professional with the drive to succeed. I have benefited from working alongside exceptional people, who have helped me develop personally, and as a leader. My goal is to engage with as many strategic and intellectual minds as possible, and to help others develop to achieve theirs.</p>
  </section>
</header>

<table class="employment">
  <thead>
    <tr class="title"><th colspan="3">EMPLOYMENT RECORD (last 15 years)</th></tr>
    <tr class="cols"><th class="col-dates">Dates</th><th class="col-role">Role</th><th>Organisation</th></tr>
  </thead>
  <tbody>
    <tr><td>May 2016<br>to current</td><td>Marketing Strategy Consultant</td><td>Clients include PedalNotes, Verdana Wellness, Harlow Sydney, Supper Sorted</td></tr>
    <tr><td>January 2011<br>to Current</td><td>Marketer &amp; Business Development</td><td>Finn Calder Photography</td></tr>
    <tr><td>August 2015<br>to May 2016</td><td>Career break</td><td></td></tr>
    <tr><td>April 2015<br>to August 2015</td><td>Head of Marketing</td><td>Northwind Life Distribution (US)<br>Selected Life (life insurance brand)</td></tr>
    <tr><td>August 2014<br>to April 2015</td><td>Maternity Leave - to my son Theo</td><td></td></tr>
    <tr><td>March2014<br>to August 2014</td><td>General Manager Marketing<br>and Business Operations</td><td>Northwind Life Distribution (UK)<br>Swift Life (life insurance brand)</td></tr>
    <tr><td>May 2103<br>to April 2014</td><td>Career Break</td><td></td></tr>
    <tr><td>October 2013</td><td>Consultant – New Business Proposal</td><td>Brightline Administration<br>Services Pty Limited</td></tr>
    <tr><td>December 2012<br>to May 2013</td><td>Commercial &amp; MIS Manager</td><td>Harbourline Limited</td></tr>
    <tr><td>July 2012<br>to December 2012</td><td>Head of Marketing Operations<br>Acquisition and Retention</td><td>Harbourline Limited</td></tr>
    <tr><td>October 2010<br>to July 2012</td><td>P&amp;L / Brand Manager<br>CoverDirect</td><td>Harbourline Limited</td></tr>
    <tr><td>January 2010<br>to October 2010</td><td>Product Portfolio Marketing Manager –<br>CoverDirect</td><td>Harbourline Limited<br>(previously KEYSTONE)</td></tr>
    <tr><td>January 2008<br>to October 2010</td><td>Marketing Manager – CoverDirect</td><td>Harbourline Limited (CoverDirect Pty Ltd was acquired by Harbourline in September 2008)</td></tr>
    <tr><td>February 2007<br>to December 2007</td><td>Database and Retention Strategy Manager</td><td>CoverDirect Pty Limited<br>Melbourne Office relocation</td></tr>
    <tr><td>July 2004<br>to January 2007</td><td>Direct Marketing Specialist</td><td>CoverDirect Pty Limited</td></tr>
    <tr><td>April 2002<br>to June 2004</td><td>Acquisition and Database Marketing<br>Manager - Japan</td><td>Primeletters Pty Ltd<br>(currently known as Postmasters Pty Ltd)</td></tr>
  </tbody>
</table>
</body>
</html>
```